Business Card Design Project

Business Card design based on logo.

I need business card, letterhead, envelope, and if possible, Powerpoint slide template.

On front of business card: Just logo- and  my name and title:  Helena Marsk, Principal

On reverse-logo and the rest of the contact info:

4871 Orchard Lane
Ashford, OR 97412
650-318-2274
hm@brevicaeducation.example

On letterhead-Just logo at top, at bottom  the rest-very small along the bottom

On PPT slide-just the logo.

I also want to try a few other colors-I like lime/dark grey (not black) but would like to try Sienna, maybe also indigo or bright blue-green.

I forgot to add-

On the business card-switch to vertical on reverse side and put:

Reverse side-switch to vertical and list:

Helena Marsk
Principal
Brevica Tutoring Partners, LLC

650-318-2274

4871 Orchard Lane
Ashford, OR 97412

Helena Marsk
Principal

650-318-2274

4871 Orchard Lane
Ashford, OR 97412

I have another project at the same time-for Stationery. Feel free to submit to that one also.

That one includes letterhead, envelope, PPT slide, folder cover sheet-HM

Industry/Entity Type

Business

Requirements
Must have
• Must use logo-preferably lime green version-with gray, not black or just 2-tone -logo on colored background.

```html
<!DOCTYPE html>
<html lang="en">
<head>
<meta charset="utf-8">
<title>Brevica Tutoring Partners – Business Card</title>
<link rel="stylesheet" href="https://fonts.googleapis.com/css2?family=Lato:wght@400;700&display=swap">
<style>
  :root {
    --backdrop: #ececec;
    --lime: #9bb82f;
    --lime-icon: #8fb030;
    --lime-text: #86a928;
    --card-white: #ffffff;
    --ink: #555759;
    --rule: #6b6d70;
    --shadow: rgba(0, 0, 0, 0.22);
  }
  html, body {
    margin: 0;
    padding: 0;
    width: 1200px;
    height: 900px;
    overflow: hidden;
    background: var(--backdrop);
    font-family: "Lato", sans-serif;
  }
  .canvas {
    position: relative;
    width: 1200px;
    height: 900px;
  }
  .card {
    position: absolute;
    box-shadow: 0 2px 6px var(--shadow);
  }

  /* Front */
  .card-front {
    left: 134px;
    top: 300px;
    width: 532px;
    height: 296px;
    background: var(--lime);
  }
  .front-wordmark {
    position: absolute;
    left: 22px;
    top: 210px;
    margin: 0;
    color: var(--card-white);
    font-weight: 400;
    font-size: 28px;
    line-height: 34px;
    letter-spacing: 6px;
    text-transform: uppercase;
  }

  /* Back */
  .card-back {
    left: 766px;
    top: 182px;
    width: 296px;
    height: 532px;
    background: var(--card-white);
    color: var(--ink);
  }
  .holder-name {
    position: absolute;
    left: 20px;
    top: 69px;
    margin: 0;
    font-size: 23px;
    font-weight: 400;
    letter-spacing: 0.3px;
    text-transform: uppercase;
  }
  .holder-role {
    position: absolute;
    left: 20px;
    top: 96px;
    margin: 0;
    font-size: 15px;
    line-height: 20px;
  }
  .divider {
    position: absolute;
    left: 18px;
    top: 157px;
    width: 238px;
    height: 0;
    border-top: 1px solid var(--rule);
  }
  .contact-line {
    position: absolute;
    left: 18px;
    display: flex;
    align-items: flex-start;
    font-size: 15px;
    line-height: 20px;
  }
  .contact-line svg {
    width: 14px;
    height: 14px;
    margin-top: 3px;
    margin-right: 10px;
    flex: none;
  }
  .contact-phone { top: 200px; }
  .contact-email { top: 220px; }
  .contact-address { top: 268px; }
  .back-wordmark {
    position: absolute;
    left: 0;
    width: 100%;
    top: 440px;
    margin: 0;
    text-align: center;
    color: var(--lime);
    font-size: 22px;
    font-weight: 400;
    letter-spacing: 2px;
    text-transform: uppercase;
  }
  .website {
    position: absolute;
    left: 0;
    width: 100%;
    top: 496px;
    margin: 0;
    text-align: center;
    font-size: 14.5px;
  }
  .website strong {
    color: var(--lime-text);
    font-weight: 700;
  }
</style>
</head>
<body>
<main class="canvas">

  <section class="card card-front" aria-label="Business card front">
    <p class="front-wordmark">Brevica<br>Tutoring</p>
  </section>

  <section class="card card-back" aria-label="Business card back">
    <h1 class="holder-name">Helena Marsk</h1>
    <p class="holder-role">Principal<br>Brevica Tutoring Partners, LLC</p>
    <div class="divider"></div>

    <div class="contact-line contact-phone">
      <svg viewBox="0 0 14 14" aria-hidden="true">
        <rect x="1" y="1" width="12" height="12" rx="1" fill="none" stroke="var(--lime-icon)" stroke-width="1.6"/>
        <rect x="3.5" y="3" width="2.5" height="8" fill="var(--lime-icon)"/>
        <rect x="7.5" y="4" width="3.5" height="1.4" fill="var(--lime-icon)"/>
        <rect x="7.5" y="7" width="3.5" height="1.4" fill="var(--lime-icon)"/>
      </svg>
      <span>650-318-2274</span>
    </div>
    <div class="contact-line contact-email">
      <svg viewBox="0 0 14 14" aria-hidden="true">
        <rect x="1" y="3" width="12" height="9" fill="none" stroke="var(--lime-icon)" stroke-width="1.4"/>
        <path d="M1 3 L7 8 L13 3 M1 12 L5.5 7 M13 12 L8.5 7" fill="none" stroke="var(--lime-icon)" stroke-width="1.2"/>
      </svg>
      <span>hm@brevicaeducation.example</span>
    </div>
    <div class="contact-line contact-address">
      <svg viewBox="0 0 14 14" aria-hidden="true">
        <path d="M7 0.8 C4.3 0.8 2.6 2.7 2.6 5 C2.6 8 7 13.2 7 13.2 C7 13.2 11.4 8 11.4 5 C11.4 2.7 9.7 0.8 7 0.8 Z" fill="var(--lime-icon)"/>
        <circle cx="7" cy="5" r="1.7" fill="var(--card-white)"/>
      </svg>
      <span>4871 Orchard Lane<br>Ashford, OR 97412</span>
    </div>

    <p class="back-wordmark">Brevica Tutoring</p>
    <p class="website">www.<strong>brevicaeducation</strong>.example</p>
  </section>

</main>
</body>
</html>
```